Mara Lindqvist Advisory Business Cards

Hi - using the information and logo provided I require a two sided business card designed with the following information. The business card is a 'mini card' 3.5" x 1.25".

Front of card should be the logo attached but inverted (so the background is the peach colour and the logo white).

Back should have these details. If we can't fit the Instragram and Facebook part can we just put the little logos.

Mara Lindqvist

Art and Design Consultant
Dealer - Curator - Events - Styling - Creative Sourcing

P: 0438 519 207
E: mara@maralindqvistadvisory.com
W: www.maralindqvistadvisory.com
I (instagram image please): maralindqvistadvisory F (Facebook image please): MaraLindqvistAdvisor

Target Market(s)

Galleries, artists, art buyers, interior design clients, event managers, creative types

Industry/Entity Type

Business

```html
<!DOCTYPE html>
<html lang="en">
<head>
<meta charset="utf-8">
<title>Mara Lindqvist Advisory – Business Card</title>
<link rel="stylesheet" href="https://fonts.googleapis.com/css2?family=Arimo:wght@400;700&display=swap">
<style>
  :root {
    --clay: #b88b75;
    --peach: #f4b89c;
    --white: #ffffff;
    --sans: "Arimo", Arial, sans-serif;
  }
  * { margin: 0; padding: 0; box-sizing: border-box; }
  html, body { width: 1200px; height: 874px; overflow: hidden; background: var(--white); }
  .card-sheet { position: relative; width: 1200px; height: 874px; background: var(--white); font-family: var(--sans); }

  /* front */
  .front { position: absolute; left: 0; top: 0; width: 1200px; height: 429px; background: var(--clay); }
  .front-arch { position: absolute; left: 0; top: 0; }
  .front-mark { position: absolute; left: 522px; top: 58px; width: 156px; height: 156px; border-radius: 50%; background: var(--white); }
  .front-name {
    position: absolute; left: 0; width: 1200px; text-align: center; color: var(--white);
    font-family: var(--sans); font-weight: 400; white-space: nowrap;
  }
  .front-name--main { top: 306px; font-size: 52px; letter-spacing: 0.16em; padding-left: 0.16em; }
  .front-name--sub { top: 381px; font-size: 30px; letter-spacing: 0.5em; padding-left: 0.5em; }

  /* back */
  .back-mark-panel { position: absolute; left: 0; top: 445px; width: 326px; height: 429px; background: var(--peach); }
  .back-mark { position: absolute; left: 105px; top: 118px; width: 116px; height: 116px; border-radius: 50%; background: var(--white); }
  .back-mark-name {
    position: absolute; left: 0; width: 326px; text-align: center; color: var(--white);
    font-weight: 400; font-size: 21px; letter-spacing: 0.12em; line-height: 30px; top: 258px;
  }

  .back-details { position: absolute; left: 337px; top: 445px; width: 863px; height: 429px; background: var(--clay); color: var(--white); }
  .person { position: absolute; left: 0; width: 863px; text-align: center; }
  .person-name { top: 40px; font-size: 32px; font-weight: 700; }
  .person-role { top: 85px; font-size: 25px; }
  .person-services { top: 123px; font-size: 25px; }

  .contacts { position: absolute; right: 40px; top: 222px; list-style: none; }
  .contact { display: flex; justify-content: flex-end; align-items: center; height: 35px; font-size: 25px; }
  .contact-icon { width: 30px; height: 30px; margin-left: 10px; flex: none; }
</style>
</head>
<body>
<main class="card-sheet">

  <section class="front">
    <svg class="front-arch" width="1200" height="429" viewBox="0 0 1200 429">
      <path d="M123,-10 L123,0 C123,250 190,429 320,429 L880,429 C1010,429 1077,250 1077,0 L1077,-10 Z"
            fill="var(--peach)" stroke="var(--white)" stroke-width="7"/>
    </svg>
    <div class="front-mark"></div>
    <p class="front-name front-name--main">MARA LINDQVIST</p>
    <p class="front-name front-name--sub">ADVISORY</p>
  </section>

  <section class="back-mark-panel">
    <div class="back-mark"></div>
    <p class="back-mark-name">MARA LINDQVIST<br>ADVISORY</p>
  </section>

  <section class="back-details">
    <h1 class="person person-name">Mara Lindqvist</h1>
    <p class="person person-role">Art and Design Consultant</p>
    <p class="person person-services">Dealer - Curator - Events - Styling - Creative Sourcing</p>

    <ul class="contacts">
      <li class="contact">0438 519 207
        <svg class="contact-icon" viewBox="0 0 30 30"><circle cx="15" cy="15" r="15" fill="var(--white)"/>
          <path d="M10,7 L13,7 L14,11 L12,13 C13,16 14,17 17,18 L19,16 L23,17 L23,20 C23,22 21,23 19,22.5 C13,21 9,17 7.5,11 C7,9 8,7 10,7 Z" fill="var(--clay)"/></svg>
      </li>
      <li class="contact">mara@maralindqvistadvisory.com
        <svg class="contact-icon" viewBox="0 0 30 30"><circle cx="15" cy="15" r="15" fill="var(--white)"/>
          <rect x="7" y="9.5" width="16" height="11" rx="1.5" fill="var(--clay)"/>
          <path d="M7.5,10.5 L15,16 L22.5,10.5" fill="none" stroke="var(--white)" stroke-width="1.5"/></svg>
      </li>
      <li class="contact">MaraLindqvistAdvisor
        <svg class="contact-icon" viewBox="0 0 30 30"><circle cx="15" cy="15" r="15" fill="var(--white)"/></svg>
      </li>
      <li class="contact">maralindqvistadvisory
        <svg class="contact-icon" viewBox="0 0 30 30"><circle cx="15" cy="15" r="15" fill="var(--white)"/></svg>
      </li>
      <li class="contact">www.maralindqvistadvisory.com
        <svg class="contact-icon" viewBox="0 0 30 30"><circle cx="15" cy="15" r="15" fill="var(--white)"/>
          <circle cx="14" cy="14" r="5.5" fill="none" stroke="var(--clay)" stroke-width="2.5"/>
          <path d="M18,18 L22,22" stroke="var(--clay)" stroke-width="3" stroke-linecap="round"/></svg>
      </li>
    </ul>
  </section>

</main>
</body>
</html>
```